Dermacare Nurse Alliance - Rack Card Design

This is a 2-sided rack card that should be 3.5 inches wide by 8.5 inches tall.

Text (with instructions), logo and website image are attached. For the main image on the front, you can use the attached image, or pull whatever you like off of stockpixelvault.example, and we will purchase the photo from the winning design

The front should have text plus a nurse image, the back should have mostly text with the website image and legend.
Updates

We have received many high quality designs, but it is apparent to us that at the print size we are currently using (3.5x8.5), that the image of the homepage on the back is too small, and not legible. As such, we have decided that we would like to go with a horizontal version at 8.5 wide by 5.5 tall, with a larger more legible version of the website on the back and call outs to one side or the other, please resubmit your designs in that format. Thank you, and sorry for the inconvenience. Ned

Industry/Entity Type

Nurse

Font styles to use
Sans Serif

Colors
876aae
6b449b
b7a5cd
e4daeb

Requirements
Must have
• Please use the color palate from the attached logo, and a nursing image on the front.

```html
<!DOCTYPE html>
<html lang="en">
<head>
<meta charset="utf-8">
<title>Dermacare Nurse Alliance – Rack Card</title>
<link rel="stylesheet" href="https://fonts.googleapis.com/css2?family=Questrial&display=swap">
<style>
  :root {
    --purple: #6b449b;
    --purple-mid: #876aae;
    --lavender: #b7a5cd;
    --lavender-pale: #e4daeb;
    --ink: #3a3a3a;
    --muted: #5e5e5e;
    --paper: #ffffff;
    --backdrop: #eeeae6;
  }
  * { box-sizing: border-box; margin: 0; padding: 0; }
  html, body { width: 1200px; height: 1000px; overflow: hidden; }
  body {
    background: var(--backdrop);
    font-family: "Questrial", Arial, sans-serif;
    position: relative;
  }
  .card {
    position: absolute;
    width: 640px;
    height: 414px;
    background: var(--paper);
    box-shadow: 0 6px 18px rgba(0,0,0,.18);
    overflow: hidden;
  }
  /* Front */
  .card--front { left: 70px; top: 46px; }
  .front__photo {
    position: absolute; left: 0; top: 0; width: 100%; height: 300px;
    background: linear-gradient(160deg, #c9936f 0%, #a8735a 35%, #2f3d6e 65%, #28335d 100%);
  }
  .front__band {
    position: absolute; left: 0; top: 300px; width: 100%; height: 22px;
    background: var(--purple);
  }
  .front__brand {
    position: absolute; right: 0; top: 240px; width: 230px; height: 82px;
    background: var(--paper);
    display: flex; align-items: center; gap: 10px; padding: 0 18px;
  }
  .brand__square { width: 16px; height: 16px; background: var(--purple); flex: none; }
  .brand__name {
    color: var(--purple); font-size: 17px; line-height: 1.15; text-transform: uppercase;
  }
  .front__tagline {
    position: absolute; left: 32px; top: 340px;
    color: var(--purple-mid); font-size: 17px; line-height: 1.3;
    list-style: none;
  }
  /* Back */
  .card--back { left: 490px; top: 520px; }
  .back__header {
    height: 82px; padding: 14px 24px;
    background: linear-gradient(90deg, var(--purple-mid), var(--purple));
    color: var(--paper); font-size: 17px; line-height: 1.45;
  }
  .back__body { display: flex; padding: 16px 22px 0; gap: 18px; }
  .back__site {
    width: 230px; height: 300px; flex: none;
    background: linear-gradient(180deg, var(--lavender-pale) 0%, #f6f3f9 55%, #d8cde4 100%);
    border: 1px solid #ddd;
  }
  .features { list-style: none; flex: 1; }
  .feature { margin-bottom: 9px; }
  .feature__title { color: var(--purple-mid); font-size: 14px; line-height: 1.15; }
  .feature__text { color: var(--muted); font-size: 10.5px; line-height: 1.3; }
</style>
</head>
<body>
  <section class="card card--front">
    <div class="front__photo" role="img" aria-label="Photo of four smiling nurses in navy scrubs with arms crossed outside a clinic"></div>
    <div class="front__band"></div>
    <div class="front__brand">
      <span class="brand__square"></span>
      <span class="brand__name">Dermacare<br>Nurse Alliance</span>
    </div>
    <ul class="front__tagline">
      <li>Inspired by patients.</li>
      <li>Empowered by knowledge.</li>
      <li>Impacting melanoma.</li>
    </ul>
  </section>

  <section class="card card--back">
    <header class="back__header">
      You wear many hats and take care of patients with many different tumor types. Check out DermacareNurse.example for free access to:
    </header>
    <div class="back__body">
      <div class="back__site" role="img" aria-label="Screenshot of the Dermacare Nurse Alliance website homepage"></div>
      <ul class="features">
        <li class="feature">
          <h3 class="feature__title">News</h3>
          <p class="feature__text">Hot off the press! Articles from the Journal of Clinical Care Nursing outlining practical strategies to manage side-effects and promote adherence to melanoma therapies</p>
        </li>
        <li class="feature">
          <h3 class="feature__title">Nursing Consensus Statements from JCCN</h3>
          <p class="feature__text">Visual and text-based therapeutic side effect management tools</p>
        </li>
        <li class="feature">
          <h3 class="feature__title">Nurse Toolkit</h3>
          <p class="feature__text">A Nurse's Toolkit with extensive melanoma nursing care resources</p>
        </li>
        <li class="feature">
          <h3 class="feature__title">Printable Patient Materials</h3>
          <p class="feature__text">Printable patient resources to provide patients, organized by therapy</p>
        </li>
        <li class="feature">
          <h3 class="feature__title">Q&amp;A Community</h3>
          <p class="feature__text">An oncology nurse community forum to share successes, challenges, insights, and solutions</p>
        </li>
        <li class="feature">
          <h3 class="feature__title">Education</h3>
          <p class="feature__text">Online educational modules, newsfeeds, and other material to keep you up to date</p>
        </li>
      </ul>
    </div>
  </section>
</body>
</html>
```